■依頼の目的/概要
鶏白湯塩ラーメンのポスター作成お願いします!

■依頼詳細
鶏白湯塩ラーメンのポスターを作成お願いします。
値段は780円です。

デザインについては特に、指定はありません。
A1のポスターです。

鶏白湯塩ラーメンについて

鶏白湯スープにじっくり時間をかけて熟成させた自家製塩タレを合わせ、アクセントにアオサを使用しました。
(こちらの文章を入れて欲しいです。)

写真はURLからダウンロードお願いします。

http://filebako.example/dl/7a1c93e0b5d2f4c8a6e1027b3d9f5c4e8a1b6d20

お店のイメージです。
こちらのお店の物になります。

https://gurumemo.example/fukuoka/B7002/B700209/51178364/

https://www.tomobook.example/torisoba.hakata/
http://filebako.example/dl/3e8d21f6c0a94b7e5d13a8f2c6b0e974d1a5c3b8

おそくなりましたこちらからダウンロードお願いしいます。
再度アップしました。こちらからダウンロードできますか?
http://filebako.example/dl/c5b07e3a91d6f2e48a0c7b15d3e9f6a2b4c81d07

とても素晴らしいデザインありがとうございます!

提案ありがとうございました!

```html
<!DOCTYPE html>
<html lang="ja">
<head>
<meta charset="utf-8">
<title>鶏白湯塩 ポスター</title>
<link rel="stylesheet" href="https://fonts.googleapis.com/css2?family=Yuji+Boku&family=Noto+Serif+JP:wght@700;900&display=swap">
<style>
  :root {
    --wood-dark: #2b160c;
    --wood-mid: #5a3220;
    --wood-light: #8a5a3c;
    --table-light: #b07a52;
    --bowl-white: #f7f4ee;
    --soup-cream: #ece4d4;
    --text-light: #ffffff;
    --price-dark: #1d1410;
  }
  * { margin: 0; padding: 0; box-sizing: border-box; }
  html, body { width: 846px; height: 1200px; overflow: hidden; }
  body { background: var(--wood-dark); }
  .poster {
    position: relative;
    width: 846px;
    height: 1200px;
    overflow: hidden;
    background: linear-gradient(180deg, var(--wood-dark) 0%, var(--wood-mid) 40%, var(--wood-light) 75%, var(--table-light) 100%);
  }
  .scene-photo {
    position: absolute;
    inset: 0;
    background:
      radial-gradient(ellipse 400px 230px at 420px 760px, var(--bowl-white) 0%, var(--soup-cream) 70%, rgba(236,228,212,0) 100%),
      radial-gradient(ellipse 460px 300px at 420px 800px, rgba(255,255,255,0.35) 0%, rgba(255,255,255,0) 100%);
  }
  .title {
    position: absolute;
    top: 70px;
    left: 0;
    width: 100%;
    text-align: center;
    font-family: "Yuji Boku", serif;
    font-size: 168px;
    line-height: 1;
    letter-spacing: 6px;
    color: var(--text-light);
  }
  .description {
    position: absolute;
    top: 262px;
    left: 78px;
    font-family: "Noto Serif JP", serif;
    font-weight: 700;
    font-size: 35px;
    line-height: 60px;
    letter-spacing: 3px;
    color: var(--text-light);
  }
  .brand {
    position: absolute;
    left: 26px;
    bottom: 60px;
    font-family: "Noto Serif JP", serif;
    font-weight: 900;
    font-size: 30px;
    line-height: 1.2;
    color: var(--price-dark);
    display: flex;
    align-items: center;
    gap: 10px;
  }
  .brand-dot { width: 16px; height: 16px; border-radius: 50%; background: var(--price-dark); }
  .price {
    position: absolute;
    right: 24px;
    bottom: 44px;
    font-family: "Noto Serif JP", serif;
    font-weight: 700;
    font-size: 76px;
    line-height: 1;
    color: var(--price-dark);
  }
</style>
</head>
<body>
  <main class="poster">
    <div class="scene-photo" role="img" aria-label="木目のテーブルに置かれた白い丼の鶏白湯塩ラーメン。アオサ、白髪ねぎ、チャーシュー、箸で持ち上げた麺"></div>
    <h1 class="title">鶏白湯塩</h1>
    <p class="description">
      鶏白湯スープにじっくり時間をかけて<br>
      熟成させた自家製塩タレを合わせ、<br>
      アクセントにアオサを使用しました。
    </p>
    <div class="brand"><span class="brand-dot"></span>鶏湯屋 TORIYU</div>
    <p class="price">¥780</p>
  </main>
</body>
</html>
```